Harrowgate Crew Outings Retractable Banner

Retractable Banner

78" high x 33" wide
1" bleed top and sides
3" bleend bottom
1080 dots/inch
RGB, JPG, PDF, EPF, PNG, TIF

See website and colors scheme at HarrowgateCrewOutings.com

Want something to be at the back of my booth during a conventions. Don't really need lots of words but just something colorful with logo and cities. Something fun and professional to grab the attention of people walking by

Not sure of the best file format so uploaded a bunch of different files.

Would like the wording from the ppt file. Outdoor Events - listed. Indoor Events - Listed.

Added pics of some of my people. Do we add these?

Target Market(s)

Vendor show - retractable banner - would like two different ones that are similar in design.

Industry/Entity Type

Building

Font styles to use
Sans Serif

Colors
f37122
ec1f27
0455a3

Requirements
Must have
• Logo top
• Want the cities names at top
• web address
• Some thing playful and fun and funky- Catch the attention of people at convention.
Nice to have
• I really would like two banners that complement each other. Only one needs the working, the other can have some of the photos of happy people.
• Wild fun design or flowing lines in background. I like the wavy lines from the PPT called "Color sample".

```html
<!DOCTYPE html>
<html lang="en">
<head>
<meta charset="utf-8">
<title>Harrowgate Crew Outings – Retractable Banner</title>
<link rel="stylesheet" href="https://fonts.googleapis.com/css2?family=Open+Sans:wght@300;400&display=swap">
<style>
  :root {
    --paper: #ffffff;
    --brand-red: #ec1f27;
    --brand-blue: #0455a3;
    --brand-orange: #f37122;
    --band-blue: #6a9fd6;
    --band-orange: #f8a436;
    --frame-blue: #6a9fd6;
    --frame-orange: #f8a436;
    --ink: #2b2b2b;
    --band-text: #ffffff;
  }
  html, body {
    margin: 0;
    padding: 0;
    width: 1200px;
    height: 2740px;
    overflow: hidden;
    background: var(--paper);
  }
  .banner {
    position: relative;
    width: 1200px;
    height: 2740px;
    background: var(--paper);
    font-family: "Open Sans", Arial, sans-serif;
  }
  .banner-frame {
    position: absolute;
    inset: 0;
  }
  .brand-mark {
    position: absolute;
    left: 0;
    top: 0;
    width: 1200px;
    height: 860px;
  }
  .brand-name {
    position: absolute;
    left: 0;
    width: 1200px;
    top: 840px;
    margin: 0;
    text-align: center;
    color: var(--brand-red);
    font-weight: 400;
    font-size: 112px;
    line-height: 134px;
    letter-spacing: -1px;
  }
  .contact {
    position: absolute;
    left: 0;
    width: 1200px;
    top: 1150px;
    text-align: center;
    color: var(--ink);
    font-size: 42px;
    line-height: 54px;
    font-weight: 400;
  }
  .contact p { margin: 0; }
  .city-bands {
    position: absolute;
    left: 0;
    top: 0;
    width: 1200px;
    height: 2740px;
  }
  .band-blue { fill: var(--band-blue); }
  .band-orange { fill: var(--band-orange); }
  .city-name {
    fill: var(--band-text);
    font-family: "Open Sans", Arial, sans-serif;
    font-weight: 300;
    font-size: 86px;
    letter-spacing: 1px;
  }
</style>
</head>
<body>
<main class="banner">

  <svg class="banner-frame" width="1200" height="2740" viewBox="0 0 1200 2740" aria-hidden="true">
    <rect x="50" y="40" width="1100" height="2640" fill="none"
          stroke="var(--frame-orange)" stroke-width="10"
          stroke-dasharray="40 40"/>
    <rect x="50" y="40" width="1100" height="2640" fill="none"
          stroke="var(--frame-blue)" stroke-width="10"
          stroke-dasharray="40 40" stroke-dashoffset="40"/>
  </svg>

  <svg class="brand-mark" width="1200" height="860" viewBox="0 0 1200 860" aria-hidden="true">
    <circle cx="600" cy="450" r="240" fill="var(--brand-orange)"/>
  </svg>

  <h1 class="brand-name">Harrowgate<br>Crew Outings</h1>

  <div class="contact">
    <p class="contact-web">HarrowgateCrewOutings.com</p>
    <p class="contact-phone">603-555-0148</p>
  </div>

  <svg class="city-bands" width="1200" height="2740" viewBox="0 0 1200 2740" role="list" aria-label="Cities served">
    <g role="listitem">
      <polygon class="band-blue" points="218,1452 982,1446 982,1598 218,1602"/>
      <text class="city-name" x="306" y="1558">PORTSMOUTH</text>
    </g>
    <g role="listitem">
      <polygon class="band-orange" points="218,1620 982,1626 982,1772 218,1774"/>
      <text class="city-name" x="306" y="1730">MANCHESTER</text>
    </g>
    <g role="listitem">
      <polygon class="band-blue" points="218,1794 982,1790 982,1946 218,1948"/>
      <text class="city-name" x="306" y="1904">CONCORD</text>
    </g>
    <g role="listitem">
      <polygon class="band-orange" points="218,1966 982,1970 982,2120 218,2118"/>
      <text class="city-name" x="306" y="2078">DURHAM</text>
    </g>
    <g role="listitem">
      <polygon class="band-blue" points="218,2140 982,2136 982,2290 218,2294"/>
      <text class="city-name" x="306" y="2250">BOSTON</text>
    </g>
    <g role="listitem">
      <polygon class="band-orange" points="218,2312 982,2318 982,2470 218,2466"/>
      <text class="city-name" x="306" y="2424">PORTLAND</text>
    </g>
  </svg>

</main>
</body>
</html>
```